Web Design Project for Film Business

We need a web design for a new company based in Bondi Beach, Sydney, Australia. We basically provide filming and video editing services. Our targets are basically corporate videos, wedding videos and other types of functions.
The important thing to know about us is that we are not just people that press the record button, we consider ourselves story tellers. We can make something boring like a conference look interesting to watch and we can also make a wedding look like a blockbuster movie that you can't look away from until its finished.
We need something as new and fresh as Bondi Beach. A young place where people come from all over the world to enjoy summer and we are lucky to be based here.
To see some of our work please visit our tavlora Channel. Make sure you watch a couple of wedding video and the corporate video so you can have a better understanding about our style.
Please note- we are not trying to market ourselves exclusively as wedding videographers, nor do we want to exploit the idea of the beach.

http://tavlora.com/channels/815374

sites that we really like:

http://www.quillpathreels.co.uk/
http://www.marnowebb.co.uk/

Target Market(s)

Couples - Corporate

Industry/Entity Type

Business

Requirements
Must have
• 5 to 6 pages (we are still deciding)
-main page
-our story (story about Karrow Films)
-your story (page designated for wedding videos)
-your business (page designated for corporate videos)
-contact us
-other stuff
Nice to have
• I would like to see some animation. Maybe you can animate our logo. Up to the designer

```html
<!DOCTYPE html>
<html lang="en">
<head>
<meta charset="utf-8">
<title>Karrow Films</title>
<link href="https://fonts.googleapis.com/css2?family=PT+Sans:wght@400;700&display=swap" rel="stylesheet">
<style>
:root{
  --page-deep:#071a27;
  --page-mid:#0e3550;
  --panel:#1e3a4e;
  --ink:#ffffff;
  --ink-soft:#c9d8e2;
  --ink-dark:#1c2a33;
  --accent:#f0a020;
  --link-blue:#1e5a86;
  --band-light:#eceeef;
  --band-dark:#c3c6c8;
  --field:#0c2232;
  --field-line:#2a4a60;
}
*{box-sizing:border-box;margin:0;padding:0}
html,body{width:667px;height:1200px;overflow:hidden}
body{
  position:relative;
  font-family:"PT Sans",sans-serif;
  color:var(--ink);
  background:
    radial-gradient(ellipse 400px 120px at 340px 1010px,rgba(40,120,170,.45),transparent 70%),
    linear-gradient(180deg,var(--page-mid) 0,var(--page-deep) 170px,#0c2a3e 500px,#102f45 900px,var(--page-deep) 1140px,#061521 1200px);
}
.abs{position:absolute}
.header-glow{left:0;top:0;width:667px;height:165px;background:radial-gradient(ellipse 420px 150px at 300px 40px,rgba(110,180,225,.5),rgba(40,110,160,.2) 55%,transparent 80%)}
.brand{left:66px;top:16px;width:160px;font-weight:700;font-size:36px;line-height:36px;color:#000;text-transform:uppercase}
.search{left:392px;top:93px;width:145px;height:18px;border-radius:3px;background:linear-gradient(#1a4a66,#0f3048);border:1px solid #2c6688;font-size:9px;color:var(--ink-soft);padding:3px 7px}
.search-btn{position:absolute;right:-1px;top:-1px;width:19px;height:18px;border-radius:3px;background:linear-gradient(#58b4ea,#2680c0)}
.main-nav{left:97px;top:130px;height:18px}
.pill{position:absolute;top:0;height:18px;border-radius:5px;background:linear-gradient(#ffffff,#d5dadd);color:var(--ink-dark);font-size:11px;line-height:18px;text-align:center;box-shadow:0 1px 2px rgba(0,0,0,.5)}
.slider{left:22px;top:168px;width:626px;height:234px;background:linear-gradient(90deg,#1a1410 0,#5a4630 30%,#c9a878 55%,#8a6a48 75%,#231a12 100%)}
.slider-arrow{width:26px;height:26px;border-radius:50%;background:#0b1a24;border:2px solid #33505f}
.slider-arrow span{position:absolute;left:4px;top:4px;width:14px;height:14px;border-radius:50%;background:#e8ecee}
.content{left:28px;top:402px;width:612px;height:343px;background:linear-gradient(180deg,#25506c 0,var(--panel) 40px,var(--panel) 100%)}
.welcome-title{left:43px;top:418px;font-size:15px;font-weight:400}
.welcome-copy{left:43px;top:443px;width:585px;font-size:7.6px;line-height:16px;color:var(--ink-soft)}
.label{font-size:12px}
.player{left:38px;top:519px;width:389px;height:219px;background:#000}
.player-screen{left:6px;top:6px;width:377px;height:190px;background:linear-gradient(180deg,#c9d4dc 0,#a9b9c4 45%,#7e93a0 62%,#6c8290 100%)}
.player-bar{left:6px;top:196px;width:377px;height:18px;background:#0d0d0d}
.tool{width:26px;height:20px;background:#1a1a1a;border:1px solid #555;border-radius:3px;font-size:5px;text-align:center;color:#fff;padding-top:12px;line-height:5px}
.thumb{border:2px solid #e6e6e6}
.clip-title{font-size:12px;line-height:16px}
.clip-age{font-size:9px;color:var(--accent);margin-top:2px}
.small-btn{width:56px;height:12px;border-radius:6px;background:linear-gradient(#fff,#cfd4d7);color:var(--ink-dark);font-size:8px;line-height:12px;text-align:center}
.other-band{left:22px;top:745px;width:624px;height:167px;background:linear-gradient(180deg,var(--band-light),var(--band-dark))}
.other-title{left:52px;top:764px;font-size:15px;font-weight:400;color:var(--link-blue)}
.other-thumb{width:128px;height:96px;border:2px solid #fff;box-shadow:0 1px 3px rgba(0,0,0,.3)}
.other-caption{width:128px;text-align:center;font-size:12px;color:var(--link-blue)}
.col-rule{width:1px;background:rgba(120,160,190,.2);top:930px;height:200px}
.col-title{font-size:11px;text-align:center}
.quote{font-size:7.6px;line-height:10.5px;width:124px;font-weight:700}
.quote .date{color:var(--accent);font-weight:400;margin-left:10px}
.avatar{width:28px;height:30px}
.field{height:19px;background:var(--field);border:1px solid var(--field-line);font-size:8px;color:var(--ink-soft);padding:4px 7px}
.btn{height:17px;border-radius:6px;background:linear-gradient(#fff,#c9d1d6);color:var(--ink-dark);font-size:12px;line-height:17px;text-align:center}
.social{width:22px;height:22px;border-radius:50%}
.bottom-rule{left:0;top:1142px;width:667px;height:1px;background:rgba(120,160,190,.25)}
.foot-link{top:1153px;font-size:9px;color:var(--ink-soft)}
.copyright{left:0;top:1183px;width:667px;text-align:center;font-size:6.5px;color:#9fb3c0}
</style>
</head>
<body>

<div class="abs header-glow" role="img" aria-label="Soft blue light background"></div>

<div class="abs brand">Karrow Films</div>

<div class="abs search">Search Channels<span class="search-btn"></span></div>

<nav class="abs main-nav">
  <span class="pill" style="left:0;width:50px">Home</span>
  <span class="pill" style="left:55px;width:74px">Our story</span>
  <span class="pill" style="left:135px;width:74px">Your story</span>
  <span class="pill" style="left:215px;width:81px">Your business</span>
  <span class="pill" style="left:301px;width:74px">Contact us</span>
  <span class="pill" style="left:380px;width:74px">Our passion</span>
</nav>

<div class="abs slider" role="img" aria-label="Film studio set with lights, cameras and crew"></div>
<div class="abs slider-arrow" style="left:8px;top:260px"><span></span></div>
<div class="abs slider-arrow" style="left:633px;top:260px"><span></span></div>

<section class="abs content"></section>
<h1 class="abs welcome-title">Welcome To Our Website</h1>
<p class="abs welcome-copy">Lorem Ipsum is simply dummy text of the printing and typesetting industry. Lorem Ipsum has been the industry's standard dummy text ever since the 1500, when an unknown printer took a galley of type and scrambled it to make a type specimen book. It has survived not only five centuries, but also the leap into electronic typesetting, remaining essentially unchanged. It was popularised ......</p>

<div class="abs label" style="left:43px;top:496px">Video</div>
<div class="abs player">
  <div class="abs player-screen" role="img" aria-label="Couple on a boat by the harbour"></div>
  <svg class="abs" style="left:160px;top:82px" width="18" height="20" aria-hidden="true"><path d="M1 1 L17 10 L1 19Z" fill="rgba(255,255,255,.85)"/></svg>
  <div class="abs tool" style="left:356px;top:6px">LIKE</div>
  <div class="abs tool" style="left:356px;top:30px">LATER</div>
  <div class="abs tool" style="left:356px;top:54px">SHARE</div>
  <div class="abs tool" style="left:356px;top:78px">EMBED</div>
  <div class="abs player-bar">
    <svg class="abs" style="left:12px;top:4px" width="10" height="10" aria-hidden="true"><path d="M0 0 L10 5 L0 10Z" fill="#fff"/></svg>
    <span class="abs" style="left:40px;top:-6px;background:#222;font-size:7px;padding:0 2px">05:17</span>
    <span class="abs" style="left:42px;top:7px;width:262px;height:5px;background:#3a3a3a"></span>
    <span class="abs" style="left:312px;top:4px;font-size:9px;font-weight:700;color:#3aa4e8">||||| HD</span>
  </div>
</div>

<div class="abs label" style="left:435px;top:499px">More Videos...</div>
<div class="abs thumb" style="left:435px;top:522px;width:60px;height:58px;background:linear-gradient(#3a3428,#7a6e58)" role="img" aria-label="Couple in a forest"></div>
<div class="abs" style="left:520px;top:525px"><div class="clip-title">Jonah+Mira<br>by Teodor Alvik</div><div class="clip-age">3 months ago</div></div>
<div class="abs thumb" style="left:435px;top:592px;width:60px;height:58px;background:linear-gradient(#3a1040,#c040c0)" role="img" aria-label="Dancers under purple lights"></div>
<div class="abs" style="left:523px;top:592px"><div class="clip-title">Callum+Renata<br>by Teodor Alvik</div><div class="clip-age">2 months ago</div></div>
<div class="abs thumb" style="left:435px;top:659px;width:60px;height:58px;background:linear-gradient(#cdd8de,#8a9aa2)" role="img" aria-label="Couple by the harbour"></div>
<div class="abs" style="left:523px;top:660px"><div class="clip-title">Elias+Noor<br>by Teodor Alvik</div><div class="clip-age">7 months ago</div></div>
<div class="abs small-btn" style="left:557px;top:717px">View more...</div>

<section class="abs other-band"></section>
<h2 class="abs other-title">Other Stuff</h2>
<svg class="abs" style="left:30px;top:834px" width="10" height="16" aria-hidden="true"><path d="M9 1 L2 8 L9 15" stroke="#fff" stroke-width="2" fill="none"/></svg>
<svg class="abs" style="left:625px;top:834px" width="10" height="16" aria-hidden="true"><path d="M1 1 L8 8 L1 15" stroke="#fff" stroke-width="2" fill="none"/></svg>
<div class="abs other-thumb" style="left:51px;top:787px;background:linear-gradient(135deg,#c8dde8,#8aa4a8)" role="img" aria-label="Friends outdoors"></div>
<div class="abs other-thumb" style="left:195px;top:787px;background:linear-gradient(135deg,#d8b8a8,#7a5a4a)" role="img" aria-label="Child holding a flower"></div>
<div class="abs other-thumb" style="left:340px;top:787px;background:linear-gradient(135deg,#6a4020,#d89a40)" role="img" aria-label="Couple with candles"></div>
<div class="abs other-thumb" style="left:486px;top:787px;background:linear-gradient(135deg,#e8c8b0,#f0b030)" role="img" aria-label="Woman with a yellow flower"></div>
<div class="abs other-caption" style="left:36px;top:886px">Other Video</div>
<div class="abs other-caption" style="left:196px;top:886px">Other Video</div>
<div class="abs other-caption" style="left:338px;top:886px">Other Video</div>
<div class="abs other-caption" style="left:485px;top:886px">Other Video</div>

<span class="abs col-rule" style="left:225px"></span>
<span class="abs col-rule" style="left:411px"></span>

<div class="abs col-title" style="left:80px;top:934px;width:100px">Testimonial</div>
<svg class="abs avatar" style="left:52px;top:963px" viewBox="0 0 28 30" aria-hidden="true"><circle cx="14" cy="8" r="7" fill="#2a7ad0"/><path d="M1 30 C1 18 27 18 27 30Z" fill="#2a7ad0"/></svg>
<p class="abs quote" style="left:92px;top:965px">Lorem Ipsum is simply dummy text of the printing and typeset-ting industry<span class="date">12-june-2011</span></p>
<svg class="abs avatar" style="left:52px;top:1008px" viewBox="0 0 28 30" aria-hidden="true"><circle cx="14" cy="8" r="7" fill="#3a3d40"/><path d="M1 30 C1 18 27 18 27 30Z" fill="#3a3d40"/></svg>
<p class="abs quote" style="left:92px;top:1010px">Lorem Ipsum is simply dummy text of the printing and typeset-ting industry<span class="date">12-june-2011</span></p>
<svg class="abs avatar" style="left:52px;top:1050px" viewBox="0 0 28 30" aria-hidden="true"><circle cx="14" cy="8" r="7" fill="#3a3d40"/><path d="M1 30 C1 18 27 18 27 30Z" fill="#3a3d40"/></svg>
<p class="abs quote" style="left:91px;top:1056px">Lorem Ipsum is simply dummy text of the printing and typeset-ting industry<span class="date">12-june-2011</span></p>

<div class="abs col-title" style="left:255px;top:934px;width:100px">News Letter</div>
<div class="abs field" style="left:252px;top:962px;width:140px">Email id</div>
<div class="abs field" style="left:252px;top:987px;width:140px">Password</div>
<div class="abs btn" style="left:276px;top:1019px;width:81px">Subscribe</div>
<div class="abs col-title" style="left:264px;top:1053px;width:100px">Connect with Us</div>
<span class="abs social" style="left:264px;top:1080px;background:#3a5a98"></span>
<span class="abs social" style="left:291px;top:1080px;background:#39a8e0"></span>
<span class="abs social" style="left:319px;top:1080px;background:#2a2a2a;border:2px solid #555"></span>
<span class="abs social" style="left:347px;top:1080px;background:#f08a20"></span>

<div class="abs col-title" style="left:461px;top:931px;width:100px">Quick Contact</div>
<div class="abs field" style="left:442px;top:959px;width:138px">Name</div>
<div class="abs field" style="left:442px;top:987px;width:138px">Email</div>
<div class="abs field" style="left:442px;top:1013px;width:162px;height:82px">Message</div>
<div class="abs btn" style="left:496px;top:1102px;width:81px">Submit</div>

<span class="abs bottom-rule"></span>
<span class="abs foot-link" style="left:136px">Home</span>
<span class="abs foot-link" style="left:194px">Our story</span>
<span class="abs foot-link" style="left:259px">Your story</span>
<span class="abs foot-link" style="left:327px">Your business</span>
<span class="abs foot-link" style="left:416px">Contact us</span>
<span class="abs foot-link" style="left:491px">Our passion</span>
<div class="abs copyright">Copyright © 2011. www.karrowfilms.com</div>

</body>
</html>
```